Business card design for a world class martial arts and group fitness facility

We need a professional and eye catching design for a business card. The card will be used in networking as well as marketing.
We are a martial arts facility offering Taekwondo, Brazilian Jiu Jitsu, and group fitness. All of our programs are geared for kids and adults.
Our Taekwondo program is lead by a Hall of Fame instructor who was Instructor of the Year in 2015.
Our Brazilian Jiu Jitsu program is lead by a wold class instructor who is also a part of the renown Brazilian KVO team.
We offer 3 focused group fitness programs: Ring striking, Pulse Fitness, and The Meadow which are all lead by certified instructors in a small group setting.
Our facility is state of the art and has been recognized as such in nationally published magazines.
Our business is named The Lantern which is the linear logo that is attached. This is the main logo. I also attached a circular logo we have used in some marketing material. Our Jiu Jitsu program is the KVO team logo. The Taekwondo program is the TORVEX Prime. It would be nice to somehow incorporate all 3 logos, but The Lantern is most important.
Industry/Entity Type
Martial Art
Contact Information for Business Card
We would like to use all 3 logos if possible but The Lantern is the most important. We would like to have a place for a staff member's name while keeping the focus on the programs we offer.
Look and feel
Each slider illustrates characteristics of the customer's brand and the style your logo design should communicate.

```html
<!DOCTYPE html>
<html lang="en">
<head>
<meta charset="utf-8">
<title>The Lantern — Business Card</title>
<link rel="stylesheet" href="https://fonts.googleapis.com/css2?family=Open+Sans:ital,wght@0,400;0,600;0,700;1,400&display=swap">
<style>
  :root {
    --backdrop: #9b9b9b;
    --card: #f0f0f0;
    --brown: #5b1e10;
    --ink: #1c1c1c;
    --text: #2e2e2e;
    --muted: #555555;
    --rule: #8a8a8a;
    --band-dark: #111111;
    --white: #ffffff;
  }
  * { box-sizing: border-box; margin: 0; padding: 0; }
  html, body {
    width: 1105px; height: 1200px; overflow: hidden;
    background: var(--backdrop);
    font-family: "Open Sans", Arial, sans-serif;
    color: var(--text);
  }
  .card {
    position: absolute;
    left: 182px;
    width: 747px; height: 425px;
    background: var(--card);
    overflow: hidden;
  }
  .card--front { top: 119px; }
  .card--back { top: 637px; }

  /* Front */
  .wordmark {
    position: absolute; left: 50px; top: 58px;
    font-weight: 700; font-size: 62px; line-height: 1;
    letter-spacing: -1px; color: var(--ink);
    text-transform: uppercase;
  }
  .person {
    position: absolute; right: 44px; top: 190px; text-align: right;
  }
  .person__name {
    font-weight: 600; font-size: 25px; color: var(--brown);
    letter-spacing: 0.5px; line-height: 1.2;
  }
  .person__rule {
    position: absolute; left: 50px; right: 44px; top: 245px;
    height: 1px; background: var(--rule);
  }
  .person__title {
    position: absolute; right: 44px; top: 250px;
    font-size: 19px; color: var(--ink); letter-spacing: 0.3px;
  }
  .contact {
    position: absolute; left: 50px; top: 262px; list-style: none;
  }
  .contact li {
    display: flex; align-items: center; gap: 10px;
    height: 28.5px; font-size: 19px; color: var(--text);
  }
  .contact svg { width: 17px; height: 17px; fill: var(--brown); flex: none; }
  .address {
    position: absolute; right: 44px; top: 305px; text-align: right;
    font-size: 19px; line-height: 28px; color: var(--text);
    font-style: normal;
  }
  .band { position: absolute; left: 0; right: 0; bottom: 0; height: 40px; }
  .band svg { display: block; width: 747px; height: 40px; }
  .band__url {
    position: absolute; left: 470px; top: 0; height: 40px;
    display: flex; align-items: center;
    font-size: 18px; letter-spacing: 2.6px; color: var(--white);
  }

  /* Back */
  .programs {
    position: absolute; left: 0; right: 0; top: 140px; height: 152px;
  }
  .program-mark {
    position: absolute; top: 0; width: 152px; height: 152px;
    display: flex; align-items: center; justify-content: center; text-align: center;
    font-weight: 700; font-size: 22px; line-height: 1.15; color: var(--ink);
    text-transform: uppercase;
  }
  .program-mark--round { border: 3px solid var(--ink); border-radius: 50%; }
  .program-mark--square { border: 3px solid var(--ink); width: 161px; height: 129px; top: 11px; }
  .program-mark--kvo { left: 105px; }
  .program-mark--lantern { left: 298px; font-size: 20px; }
  .program-mark--torvex { left: 482px; }
  .tagline {
    position: absolute; left: 0; right: 0; top: 332px; text-align: center;
    font-style: italic; font-size: 20px; line-height: 27px; color: var(--muted);
  }
</style>
</head>
<body>

<section class="card card--front" aria-label="Business card front">
  <div class="wordmark">The Lantern</div>

  <div class="person">
    <p class="person__name">MARCUS HALE</p>
  </div>
  <div class="person__rule"></div>
  <p class="person__title">CEO/FOUNDER</p>

  <ul class="contact">
    <li>
      <svg viewBox="0 0 24 24" aria-hidden="true"><path d="M6.6 10.8a15.1 15.1 0 0 0 6.6 6.6l2.2-2.2c.3-.3.7-.4 1-.2 1.1.4 2.3.6 3.6.6.6 0 1 .4 1 1V20c0 .6-.4 1-1 1A17 17 0 0 1 3 4c0-.6.4-1 1-1h3.5c.6 0 1 .4 1 1 0 1.3.2 2.5.6 3.6.1.3 0 .7-.2 1z"/></svg>
      <span>555 214 7730</span>
    </li>
    <li>
      <svg viewBox="0 0 24 24" aria-hidden="true"><path d="M7 1h10a2 2 0 0 1 2 2v18a2 2 0 0 1-2 2H7a2 2 0 0 1-2-2V3a2 2 0 0 1 2-2zm0 3v14h10V4zm5 15.5a1.2 1.2 0 1 0 0 2.4 1.2 1.2 0 0 0 0-2.4z"/></svg>
      <span>555 382 6041</span>
    </li>
    <li>
      <svg viewBox="0 0 24 24" aria-hidden="true"><path d="M6 2h12v6H6zM3 9h18a2 2 0 0 1 2 2v7h-4v4H5v-4H1v-7a2 2 0 0 1 2-2zm4 7v4h10v-4z"/></svg>
      <span>555 907 3158</span>
    </li>
    <li>
      <svg viewBox="0 0 24 24" aria-hidden="true"><path d="M2 5h20v14H2zm2 2v.5l8 5 8-5V7zm0 2.8V17h16V9.8l-8 5z"/></svg>
      <span>hello@lanterngym.com</span>
    </li>
  </ul>

  <address class="address">
    4120 Birchwood Road<br>
    Fairbanks, Alaska 99701
  </address>

  <div class="band">
    <svg viewBox="0 0 747 40" aria-hidden="true">
      <rect x="0" y="13" width="420" height="15" fill="var(--brown)"/>
      <polygon points="414,0 747,0 747,40 385,40" fill="var(--band-dark)"/>
    </svg>
    <span class="band__url">www.lanterngym.com</span>
  </div>
</section>

<section class="card card--back" aria-label="Business card back">
  <div class="programs">
    <div class="program-mark program-mark--round program-mark--kvo">KVO</div>
    <div class="program-mark program-mark--round program-mark--lantern">The<br>Lantern</div>
    <div class="program-mark program-mark--square program-mark--torvex">TORVEX<br>Prime</div>
  </div>
  <p class="tagline">
    Martial arts facility offering<br>
    Taekwondo, Brazilian Jiu Jitsu &amp; group fitness
  </p>
</section>

</body>
</html>
```